Algae Cream Package Concept

Creative Brief — Solvane: Phytoplankton Rescue Cream (100 ml)
Product Snapshot
Name: Solvane: Phytoplankton Rescue Cream
Format: 100 ml / 3.4 fl oz tube or airless pump (dieline provided)
Dieline attached:
Purpose & Key Benefits
Rescue dry or damaged skin—especially eczema & psoriasis.
All‑over use: hands, feet, elbows, knees, face, body.
Repairs barrier · Deep hydration · Calms irritation · Antioxidant shield.
Usage
Longevity: ~30 days when used daily on 10 in² of skin.
How: Apply pea‑size to clean, damp skin; massage ≥1 min; reapply as needed.
Ingredients
Label Ingredients:
Aloe Barbadensis (Aloe) Leaf Juice, Butyrospermum Parkii (Shea) Butter, Aqua (and) Propanediol (and) Nannochloropsis Gaditana (Phytoplankton) Extract, Simmondsia Chinensis (Jojoba) Seed Oil, Sodium Lactate, Cetyl Alcohol, Cetearyl Olivate (and) Sorbitan Olivate (Kestrim 2400), Panthenol (Vitamin B5), Gluconolactone (and) Sodium
Benzoate (and) Calcium Gluconate (Pramicor Max), Illite (French Green Clay).
Look & Feel (for designer)
Minimal, ocean‑inspired, premium yet approachable. Off‑white base, deep‑teal accent, subtle algae texture.
Must‑Haves on Pack
Product name + “Rescue Cream” descriptor
Net weight (100 ml / 3.4 fl oz)
Tagline: “Reunite your skin with Earth’s base nutrition.”
Copy snippet: “Powered by sustainably grown phytoplankton.”
Icons: Vegan • Cruelty‑Free • Reef‑Safe • Recyclable
www.mirelbloomhaus.com

```html
<!DOCTYPE html>
<html lang="en">
<head>
<meta charset="utf-8">
<title>Solvane Phytoplankton Rescue Cream — Label</title>
<link rel="stylesheet" href="https://fonts.googleapis.com/css2?family=Oswald:wght@400;500&family=Montserrat:wght@600&family=Lato:wght@400;700&display=swap">
<style>
  :root {
    --canvas: #ffffff;
    --label-bg: #f8f6f0;
    --teal-deep: #2b5c6e;
    --ink: #2f3b42;
    --green: #4f8a2e;
    --band-start: #2f6478;
    --band-end: #5a9a34;
    --wave-green: #cfe0bd;
    --wave-teal: #d4e9e6;
  }
  * { margin: 0; padding: 0; box-sizing: border-box; }
  html, body { width: 1200px; height: 1154px; overflow: hidden; background: var(--canvas); }
  .label {
    position: absolute; left: 75px; top: 472px;
    width: 1050px; height: 210px;
    background: var(--label-bg); overflow: hidden;
  }
  .algae-texture { position: absolute; inset: 0; width: 100%; height: 100%; }
  .brand {
    position: absolute; left: 202px; top: 31px;
    width: 44px; height: 150px;
    display: flex; align-items: center; justify-content: center;
  }
  .brand span {
    transform: rotate(-90deg); white-space: nowrap;
    font-family: "Oswald", sans-serif; font-weight: 500;
    font-size: 54px; letter-spacing: 1px; line-height: 1;
    color: var(--teal-deep);
  }
  .front { position: absolute; left: 267px; top: 34px; width: 151px; }
  .front .kicker {
    font-family: "Montserrat", sans-serif; font-weight: 600;
    font-size: 14.5px; letter-spacing: 1.1px; color: var(--green); line-height: 1.1;
  }
  .front .product {
    font-family: "Oswald", sans-serif; font-weight: 400;
    font-size: 26px; letter-spacing: 1.2px; color: var(--ink); line-height: 1.15;
    margin-top: 1px;
  }
  .tagline-band {
    margin-top: 6px; height: 17px;
    background: linear-gradient(90deg, var(--band-start), var(--band-end));
    color: #fff; font-family: "Oswald", sans-serif; font-size: 5.6px;
    letter-spacing: 0.5px; display: flex; align-items: center; justify-content: center;
    text-transform: uppercase;
  }
  .benefits { display: flex; gap: 4px; margin-top: 15px; }
  .benefit { display: flex; align-items: center; gap: 2px; }
  .benefit svg { width: 9px; height: 9px; flex: none; }
  .benefit p {
    font-family: "Lato", sans-serif; font-size: 4.6px; line-height: 1.05; color: var(--ink);
  }
  .powered {
    margin-top: 18px; font-family: "Lato", sans-serif; font-weight: 700;
    font-size: 6.4px; color: var(--ink);
  }
  .volume {
    margin-top: 17px; font-family: "Lato", sans-serif; font-weight: 700;
    font-size: 7.4px; color: var(--ink);
  }
  .back { position: absolute; left: 694px; top: 24px; width: 290px; color: var(--ink); }
  .back h2 {
    font-family: "Oswald", sans-serif; font-weight: 400; font-size: 11.4px;
    color: var(--green); line-height: 1.4; margin-bottom: 4px;
  }
  .back p {
    font-family: "Lato", sans-serif; font-size: 9.2px; line-height: 12px;
    text-align: justify;
  }
  .back strong { font-weight: 700; }
</style>
</head>
<body>
  <section class="label">
    <svg class="algae-texture" viewBox="0 0 1050 210" preserveAspectRatio="none" role="img" aria-label="Subtle flowing algae wave-line texture">
      <defs>
        <radialGradient id="wave-left" cx="0.18" cy="0.75" r="0.35">
          <stop offset="0" stop-color="var(--wave-green)" stop-opacity="0.7"/>
          <stop offset="1" stop-color="var(--wave-green)" stop-opacity="0"/>
        </radialGradient>
        <radialGradient id="wave-mid" cx="0.58" cy="0.4" r="0.3">
          <stop offset="0" stop-color="var(--wave-teal)" stop-opacity="0.8"/>
          <stop offset="1" stop-color="var(--wave-teal)" stop-opacity="0"/>
        </radialGradient>
      </defs>
      <rect width="1050" height="210" fill="url(#wave-left)"/>
      <rect width="1050" height="210" fill="url(#wave-mid)"/>
    </svg>

    <div class="brand"><span>SOLVANE</span></div>

    <div class="front">
      <p class="kicker">PHYTOPLANKTON</p>
      <h1 class="product">RESCUE CREAM</h1>
      <div class="tagline-band">Reunite your skin with Earth’s base nutrition</div>
      <ul class="benefits">
        <li class="benefit">
          <svg viewBox="0 0 10 10"><circle cx="5" cy="5" r="4" fill="none" stroke="#4f8a2e" stroke-width="0.8"/><path d="M1.5 4h7M1.5 6h7" stroke="#4f8a2e" stroke-width="0.7"/></svg>
          <p>Repairs<br>barrier</p>
        </li>
        <li class="benefit">
          <svg viewBox="0 0 10 10"><path d="M5 1C3 4 2 5.5 2 6.8a3 3 0 0 0 6 0C8 5.5 7 4 5 1z" fill="none" stroke="#4f8a2e" stroke-width="0.8"/></svg>
          <p>Deep<br>hydration</p>
        </li>
        <li class="benefit">
          <svg viewBox="0 0 10 10"><path d="M5 8.5C2 7 1 4.5 1.5 2.5 4 3 5 5 5 8.5zM5 8.5C8 7 9 4.5 8.5 2.5 6 3 5 5 5 8.5z" fill="none" stroke="#4f8a2e" stroke-width="0.8"/></svg>
          <p>Calms<br>irritation</p>
        </li>
        <li class="benefit">
          <svg viewBox="0 0 10 10"><path d="M5 1l3.5 1.3v2.8C8.5 7 7 8.3 5 9 3 8.3 1.5 7 1.5 5.1V2.3z" fill="none" stroke="#4f8a2e" stroke-width="0.8"/></svg>
          <p>Antioxidant<br>shield</p>
        </li>
      </ul>
      <p class="powered">Powered By Sustainably Grown Phytoplankton</p>
      <p class="volume">100 ml / 3.4 fl oz</p>
    </div>

    <div class="back">
      <h2>Rescue dry or damaged skin—especially eczema &amp; psoriasis.</h2>
      <p>All-over use: hands, feet, elbows, knees, face, body.</p>
      <p><strong>Longevity:</strong> ~30 days when used daily on 10 in² of skin.</p>
      <p><strong>How:</strong> Apply pea-size to clean, damp skin; massage ≥1 min; reapply as needed.</p>
      <p><strong>Ingredients:</strong> Aloe Barbadensis (Aloe) Leaf Juice, Butyrospermum Parkii (Shea) Butter, Aqua (and) Propanediol (and) Nannochloropsis Gaditana (Phytoplankton) Extract, Simmondsia Chinensis (Jojoba) Seed Oil, Sodium Lactate, Cetyl Alcohol, Cetearyl Olivate (and) Sorbitan Olivate (Kestrim 2400), Panthenol (Vitamin B5), Gluconolactone (and) Sodium Benzoate (and) Calcium Gluconate (Pramicor Max), Illite (French Green Clay).</p>
    </div>
  </section>
</body>
</html>
```